Marketing / Informational Site for Marriage and Family Therapists Cooperative

We need a web design for a new Marriage and Family Therapist Cooperative, called Meadowgate Counselors. This is a market and information site for potential clients and referrals to learn more about the team and get contact information.

We are looking for profession, clean, and modern design, that cater towards families and mom's concerned about their families mental health and child development.

This should include a home page, an general about page, 3 bio pages (1 for each therapist listed below), and a general contact us page.

Our Domain Name

Meadowgatecounselors.example

Company Name

Meadowgate Counselors

Group Moto/Philosophy

“Our sorrows and wounds are healed only when we touch them with compassion.” - Orvelan

Our Logo

See Heron Final (attached)

Home Page (Introduction)

Feeling stressed and overwhelmed?
Encountering barriers towards your goals?
Having difficulty accomplishing the simplest task?
Have the need to talk but unsure who to turn to?

Therapy can assist you in overcoming all of these challenges. Assist you in uncovering the difficulties and barriers that are keeping you from achieving your life’s ambitions, help discover ways to overcome them, and cope with the impact your behaviour has on your occupation, personal life and social life.

Welcome to our practice, with over 20 years of combined experience in the clinical field you are sure to find the right fit for your needs. Each clinician has experience working with groups, adults, teens, children, families, and couples. We specialize in fostering healthy relationships between individuals, managing depression and anxiety, overcoming trauma, and developing occupational success. Feel free to explore information about each clinician and make an appointment with one of us today.

About Us (bio pics attached)

Marisel Dunkworth

My name is Dr. MariSel Dunkworth and I am a Licensed Marriage Family Therapist with a practice in Riverside, CA. I have devoted my life’s work into developing my skills in this profession. I have over 15 years of experience working in the clinical and the social service settings. These years have afforded me the opportunity to work with groups, families, adults, teens and children with varying symptoms. I have helped clients that have trauma, abuse histories, and many within the legal or social service systems. I enjoy working individuals from all walks of life achieve self sufficiency, social success and occupational success. In my years of training I have come to develop a culturally sensitive practice that centers around the needs of the client.

I have held many positions in my clinical career beginning as clinician moving upwards toward supervisor and program coordinator. I have also over 5 years of experience as an adjunct faculty member in the University setting teaching student to become Marriage and Family Therapists. As a clinician I focused on enriching my clinical skills by developing outcome driven practices to achieve client’s desired goals. As a clinical supervisor, I guided clinicians along their own paths towards clinical licensure. As a program coordinator, I helped develop a clinical assessment and triage program from ground up to assist client in accessing services in the South Los Angeles Area. The program would assist over 100 plus clients on a monthly basis get connected to clinical services and linked to any additional resources as needed by the individual. I have graduated with my, Bachelor’s degree at the Halvern College, Riverside. I received my Masters degree in Clinical Psychology at Mount St. Mary’s University, and my Doctorate degree in Clinical Psychology at Tamsworth Institute.

To schedule an appointment with Dr. MariSel Dunkworth, LMFT:

email: marisel582@postbox.example
Phone: (951)555-0182

Jeb Kowal

My name is Rosalindra (Jeb) Kowal, I received my Masters Degree of Counseling in Marriage and Family Therapy from Corvell Bay State College in June 2000. I have acquired over 15 years of experience helping Individuals, Couples, and Families cope with issues of Anxiety, Depression, Grief and Bereavement, and HIV/AIDS.

I am a Family Systems Therapist and I truly believe the dynamics in our family of origin greatly shape our current belief systems and behaviors. However, I often utilize a variety of approaches to help my clients achieve their goals depending on their individual needs.

My greatest strength as a Marriage and Family Therapist is helping my clients explore ways to make the changes in their lives that will allow them to live their life to their fullest potential. I help my clients achieve their personal life goals with a warm, safe, non-judgmental , and supportive environment. In doing so, my clients are encouraged to explore the issues that may be preventing them from living the life they desire. Thus, empowering them to take control of their personal journey to living a productive and meaningful life.

If you feel that you are ready to commit to bringing about positive changes in your life and would like support in exploring this path, I’m here to work with you in your journey to personal growth and development.

To schedule an appointment with Rosalindra Kowal, LMFT:

e-mail: rkjeb7@mailnest.example
Phone: (951)555-0147

Dena Holcroft

Dena Holcroft graduated with a Masters in Marriage and Family Therapy from Pellridge Crestwood College. She currently holds a license in Marriage and Family Therapy in the State of California. She is also formally trained in Clinical Art Therapy. Dena's expertise lies in providing treatment to individuals experiencing work-related injuries, severe physical and emotional pain, trauma, grief and loss, anxiety and depression. In her early career, she provided valuable service at the largest free clinic in the nation serving marginalized families and children. For the past ten years, Dena has worked with HIV/AIDS population.
Dena comes from a multicultural background and she has utilized this experience and knowledge in serving a variety of populations. At an organizational level, Dena has worked extensively with challenging issues such as the chemical dependency and homelessness. In her private practice, Dena is proficient in working within individuals experiencing relationship concerns, marital and family conflict, depression/anxiety, self-esteem concerns, adjustment disorders, and pain management. She has treated clients from diverse cultural, linguistic backgrounds and sexual orientations.
Dena is trained in Family Systems Theory and incorporates other strategies appropriate for each presenting issue. She specializes in Clinical Art Therapy and has successfully utilized an integrated approach including guided imagery and relaxation skills training for many years.

To schedule an appointment with Dena Holcroft, LMFT

e-mail: greypinestudio@inkmail.example
Phone: (951) 555-0169

Target Market(s)

Families with child development, marriage issues, or other mental health needs

Industry/Entity Type

Marketing

Number of Pages Required

5+ page

Requirements
Must have
• 1 home page, 1 about page, 1 contact page. About page could either be standalone page with 3 different bio pages for each therapist or an all in one about page that includes bios for all 3 therapists.

```html
<!DOCTYPE html>
<html lang="en">
<head>
<meta charset="utf-8">
<title>Meadowgate Counselors</title>
<link rel="stylesheet" href="https://fonts.googleapis.com/css2?family=Raleway:ital,wght@0,300;0,400;0,600;0,700;1,300&display=swap">
<style>
:root{
  --teal:#8fc9cd;
  --teal-soft:#b4dcdf;
  --teal-deep:#5fa6ab;
  --ink:#333a3d;
  --ink-soft:#5b6366;
  --rule:#d9dfe0;
  --white:#ffffff;
  --paper:#f7f8f8;
  --quote-dark:#3a3b39;
  --quote-mid:#5e5f5a;
}
*{box-sizing:border-box;margin:0;padding:0}
html,body{width:845px;height:1200px;overflow:hidden;background:var(--white)}
body{font-family:"Raleway",sans-serif;color:var(--ink)}
.site{width:845px;height:1200px;position:relative}

.site-header{height:85px;display:flex;align-items:flex-start;justify-content:space-between;padding:0 85px 0 85px;background:var(--white)}
.brand{display:flex;flex-direction:column;align-items:center;margin-top:14px;gap:5px}
.brand-mark{width:30px;height:30px;border-radius:50%;background:var(--teal-soft)}
.brand-name{font-size:9px;font-weight:600;letter-spacing:1px;color:var(--teal-deep);text-transform:uppercase}
.main-nav{display:flex;height:60px}
.main-nav a{display:flex;align-items:center;padding:0 12px;font-size:10px;font-weight:600;color:var(--ink);text-decoration:none;text-transform:uppercase;letter-spacing:.3px}
.main-nav a.is-active{background:var(--teal-soft);color:var(--white);position:relative}
.main-nav a.is-active::after{content:"";position:absolute;left:50%;bottom:-6px;margin-left:-6px;border-left:6px solid transparent;border-right:6px solid transparent;border-top:6px solid var(--teal-soft)}

.hero{position:relative;height:415px}
.hero-photo{position:absolute;inset:0;background:
  radial-gradient(ellipse at 62% 45%,#e8e2d6 0%,#cfc7b0 18%,rgba(160,150,80,0) 40%),
  radial-gradient(ellipse at 90% 30%,#9bb23e 0%,rgba(120,140,40,0) 45%),
  linear-gradient(180deg,#5d6a2a 0%,#8a8c2f 40%,#b8892a 72%,#8a5a1c 100%)}
.hero-copy{position:absolute;left:85px;top:112px;width:240px;color:var(--white)}
.hero-title{font-size:22px;font-weight:700;letter-spacing:.5px;margin-bottom:10px}
.hero-text{font-size:10px;line-height:1.45}
.hero-dots{position:absolute;left:50%;bottom:10px;display:flex;gap:5px;transform:translateX(-50%)}
.hero-dots span{width:5px;height:5px;border-radius:50%;background:rgba(255,255,255,.55)}
.hero-dots span.is-current{background:var(--white)}

.content{display:flex;padding:0 85px;height:455px}
.features{width:300px;padding-top:35px;flex-shrink:0}
.feature{padding:14px 0 16px;border-bottom:1px solid var(--rule)}
.feature:last-child{border-bottom:none}
.feature-head{display:flex;align-items:center;gap:14px;margin-bottom:10px}
.feature-icon{width:26px;height:22px}
.feature-title{font-size:17px;font-weight:600;color:var(--ink)}
.feature-text{font-size:9.5px;line-height:1.5;color:var(--ink-soft);width:240px}

.welcome{margin-left:85px;width:290px;padding-top:42px}
.welcome-lead{font-size:23px;font-weight:300;color:var(--ink)}
.welcome-title{font-size:23px;font-weight:700;color:var(--ink);margin-bottom:14px}
.welcome p{font-size:8.4px;line-height:1.45;color:var(--ink-soft);margin-bottom:8px}

.motto{position:relative;height:158px}
.motto-photo{position:absolute;inset:0;background:linear-gradient(100deg,var(--quote-dark) 0%,var(--quote-mid) 45%,#6d6c64 70%,var(--quote-dark) 100%)}
.motto-copy{position:absolute;inset:0;display:flex;flex-direction:column;align-items:center;justify-content:center;color:var(--white);text-align:center}
.motto-quote{font-size:19px;font-weight:300;line-height:1.3;width:560px}
.motto-author{margin-top:10px;font-size:11px;font-weight:700}

.site-footer{height:87px;background:var(--teal);display:flex;align-items:center;justify-content:space-between;padding:0 85px}
.copyright{font-size:9px;color:var(--ink)}
.footer-nav{display:flex;gap:6px;font-size:9.5px;color:var(--ink)}
.footer-nav a{color:var(--ink);text-decoration:none}
</style>
</head>
<body>
<div class="site">
  <header class="site-header">
    <div class="brand">
      <span class="brand-mark"></span>
      <span class="brand-name">Meadowgate</span>
    </div>
    <nav class="main-nav">
      <a href="#">Home</a>
      <a href="#" class="is-active">About Us</a>
      <a href="#">Services</a>
      <a href="#">Gallery</a>
      <a href="#">Contact</a>
    </nav>
  </header>

  <section class="hero">
    <div class="hero-photo" role="img" aria-label="Photo of an older couple sitting together in an autumn park"></div>
    <div class="hero-copy">
      <h1 class="hero-title">LOREM IPSUM DOLOR</h1>
      <p class="hero-text">A calm, caring space where individuals, couples and families can talk openly, heal at their own pace and find new ways forward together.</p>
    </div>
    <div class="hero-dots"><span></span><span class="is-current"></span><span></span></div>
  </section>

  <main class="content">
    <div class="features">
      <div class="feature">
        <div class="feature-head">
          <svg class="feature-icon" viewBox="0 0 26 22" fill="none" stroke="#8a9598" stroke-width="1.6">
            <circle cx="9" cy="6" r="4"/><path d="M1 21c0-5 4-8 8-8s8 3 8 8"/>
            <circle cx="19" cy="7" r="3"/><path d="M18 13c4 0 7 3 7 7"/>
          </svg>
          <h2 class="feature-title">About Us</h2>
        </div>
        <p class="feature-text">Three licensed family therapists sharing decades of clinical care for adults, teens and children.</p>
      </div>
      <div class="feature">
        <div class="feature-head">
          <svg class="feature-icon" viewBox="0 0 26 22" fill="none" stroke="#8a9598" stroke-width="1.6">
            <circle cx="13" cy="11" r="4"/>
            <path d="M13 1v4M13 17v4M3 11h4M19 11h4M6 4l3 3M17 15l3 3M20 4l-3 3M9 15l-3 3"/>
          </svg>
          <h2 class="feature-title">Services</h2>
        </div>
        <p class="feature-text">Support for anxiety, depression, trauma, grief, couples conflict and family changes of every kind.</p>
      </div>
      <div class="feature">
        <div class="feature-head">
          <svg class="feature-icon" viewBox="0 0 26 22" fill="none" stroke="#8a9598" stroke-width="1.6">
            <rect x="1.5" y="2.5" width="23" height="17" rx="1.5"/>
            <path d="M3 18l7-7 5 5 3-3 5 5"/><circle cx="18" cy="7.5" r="2"/>
          </svg>
          <h2 class="feature-title">Gallery</h2>
        </div>
        <p class="feature-text">A look inside our quiet offices in Riverside, designed to help every visitor feel at ease.</p>
      </div>
    </div>

    <article class="welcome">
      <div class="welcome-lead">Welcome to</div>
      <h2 class="welcome-title">Meadowgate Counselors</h2>
      <p>Feeling stressed and overwhelmed?<br>Encountering barriers towards your goals?<br>Having difficulty accomplishing the simplest task?<br>Have the need to talk but unsure who to turn to?</p>
      <p>Therapy can assist you in overcoming all of these challenges. Assist you in uncovering the difficulties and barriers that are keeping you from achieving your life’s ambitions, help discover ways to overcome them, and cope with the impact your behaviour has on your occupation, personal life and social life.</p>
      <p>Welcome to our practice, with over 20 years of combined experience in the clinical field you are sure to find the right fit for your needs. Each clinician has experience working with groups, adults, teens, children, families, and couples. We specialize in fostering healthy relationships between individuals, managing depression and anxiety, overcoming trauma, and developing occupational success. Feel free to explore information about each clinician and make an appointment with one of us today.</p>
    </article>
  </main>

  <section class="motto">
    <div class="motto-photo" role="img" aria-label="Dark, softly lit background photo"></div>
    <div class="motto-copy">
      <blockquote class="motto-quote">“Our sorrows and wounds are healed only when we touch them with compassion.”</blockquote>
      <div class="motto-author">- Orvelan -</div>
    </div>
  </section>

  <footer class="site-footer">
    <p class="copyright">Copyright © 2015 - Meadowgate Counselors. All rights reserved.</p>
    <nav class="footer-nav">
      <a href="#">Home</a><span>|</span><a href="#">About Us</a><span>|</span><a href="#">Services</a><span>|</span><a href="#">Gallery</a><span>|</span><a href="#">Contact</a>
    </nav>
  </footer>
</div>
</body>
</html>
```